GUARANTEED! Simple website for independent event planner and consultant...

I need a website that is no more than 5 or 6 pages to illustrate who I am and what I can offer to groups who book hotels for meetings and conferences. I have 20 years of experience planning meetings within hotels and I am now ready to go out on my own and help clients choose venues, negotiate contracts and plan effective meetings. I will focus on clients planning meetings in the mountains of Colorado but I am willing to travel as well. I want to work with a person who is collaborative and can direct me on what they need to move the project along quickly. I already have my logo, a hosting site and work e-mail address. Also, I recently hired a photographer to do head shots. Lastly, it important for me to be able to talk on the phone or skype with this person, as needed and I must be able to make changes to my site down the road when necessary...

Target Market(s)

Corporate Groups

Industry/Entity Type

Event Planning

Coding

Coded - Design and coding required

Number of Pages Required

5+ page

Font styles to use
Sans Serif

Requirements
Must have
• About me page, event planning services offered page, task force and consulting work page, testimonials page, page for blogs, page to contact me/request a proposal. May need advice on what else I need...
Nice to have
• I want it to look sharp and professional. I want people to look at my site and know immediately that they can trust me and the work I can do.
• I don't want it to look like it is over the top as I am not a HUGE company but I do want it to be professional and easy to view and navigate.
Should not have
• Bright colors
• My logo is bright orange and black. I have also used dark grey and orange. See below:
• Orange:
• C = 0
• M = 64
• Y = 100
• K = 0
• Gray:
• C = 67
• M = 60
• Y = 59
• K = 45
• Font: Gotham Book and Gotham Bold

```html
<!DOCTYPE html>
<html lang="en">
<head>
<meta charset="utf-8">
<title>Harlow Event Management</title>
<link href="https://fonts.googleapis.com/css2?family=Open+Sans:wght@300;400;600&display=swap" rel="stylesheet">
<style>
:root{
  --orange:#f47920;
  --orange-soft:rgba(244,121,32,.75);
  --ink:#333;
  --text:#555;
  --muted:#777;
  --line:#e3e3e3;
  --panel:#f5f5f5;
  --white:#fff;
}
*{margin:0;padding:0;box-sizing:border-box}
html,body{width:801px;height:1200px;overflow:hidden;background:var(--white)}
body{font-family:"Open Sans",Arial,sans-serif;color:var(--text);position:relative}
.abs{position:absolute}
.topbar{left:0;top:0;width:801px;height:19px;border-bottom:1px solid var(--line);font-size:6px;color:#666;display:flex;align-items:center;padding-left:76px;gap:10px}
.topbar span{display:flex;align-items:center;gap:3px}
.header{left:0;top:19px;width:801px;height:56px}
.brand-name{left:76px;top:19px;font-size:14px;font-weight:600;color:var(--ink);line-height:18px;white-space:nowrap}
.nav{top:23px;left:0;width:801px;font-size:6.6px;font-weight:600;color:var(--ink)}
.nav a{color:inherit;text-decoration:none;position:absolute;white-space:nowrap}
.nav a.active{color:var(--orange)}
.hero{left:0;top:75px;width:790px;height:428px;background:radial-gradient(ellipse at 50% 35%,#f59a25 0%,#d0560f 30%,#5a1a05 65%,#140502 100%)}
.frame-outer{left:99px;top:170px;width:385px;height:198px;border:14px solid var(--orange)}
.frame-inner{left:134px;top:230px;width:321px;height:83px;background:var(--orange-soft)}
.hero-title{left:134px;top:230px;font-size:27px;font-weight:300;color:var(--white);line-height:39px;white-space:nowrap}
.person{left:488px;top:165px;width:92px;height:220px;background:linear-gradient(#2a2a2a,#111);border-radius:40px 40px 6px 6px}
.btn{left:410px;top:373px;width:73px;height:22px;background:var(--white);border-radius:3px;font-size:6px;color:#444;display:flex;align-items:center;justify-content:center}
.arrow{top:280px;width:20px;height:20px;background:rgba(0,0,0,.35);display:flex;align-items:center;justify-content:center}
.feature{top:517px;width:152px;text-align:center}
.icon{width:38px;height:38px;border:1px solid #ccc;border-radius:50%;margin:0 auto;display:flex;align-items:center;justify-content:center}
.feature h3{font-size:9.5px;font-weight:400;color:var(--ink);margin-top:16px;white-space:nowrap}
.feature p{font-size:6.8px;line-height:13.3px;color:var(--muted);margin-top:8px}
.rule{left:76px;top:664px;width:648px;height:1px;background:var(--line)}
.section-title{width:801px;text-align:center;font-size:13.5px;font-weight:400;color:var(--ink)}
.section-text{left:76px;width:648px;text-align:center;font-size:6.8px;line-height:13.5px;color:var(--text)}
.boardroom{left:76px;top:768px;width:648px;height:218px;background:linear-gradient(100deg,#c08550 0%,#a8703f 35%,#e9e4dc 55%,#3b3a38 80%,#1f1f1f 100%)}
.showcase{left:0;top:986px;width:801px;height:214px;background:var(--panel)}
.thumb{top:1109px;width:146px;height:91px}
.play{position:absolute;left:55px;top:30px;width:36px;height:20px;background:rgba(0,0,0,.7);border-radius:4px;display:flex;align-items:center;justify-content:center}
</style>
</head>
<body>
<div class="abs topbar">
  <span><svg width="5" height="7" viewBox="0 0 5 7"><path d="M2.5 0a2.5 2.5 0 0 0-2.5 2.5C0 4.4 2.5 7 2.5 7S5 4.4 5 2.5A2.5 2.5 0 0 0 2.5 0z" fill="#444"/></svg>418 Aspen Ridge Circle, CO 80424, United States</span>
  <span><svg width="6" height="6" viewBox="0 0 6 6"><path d="M1 0l1.3 1.6-.7.9a4 4 0 0 0 2 2l.9-.7L6 5 5 6C2 6 0 4 0 1z" fill="#444"/></svg>+1 555-014-2290</span>
  <span><svg width="7" height="5" viewBox="0 0 7 5"><rect width="7" height="5" fill="#444"/><path d="M0 0l3.5 2.7L7 0" stroke="#fff" stroke-width=".6" fill="none"/></svg>hello@harlowevents.example</span>
</div>

<header class="abs header">
  <div class="abs brand-name">Harlow Event Management</div>
  <nav class="abs nav">
    <a class="active" style="left:266px">HOME</a>
    <a style="left:304px">ABOUT ME</a>
    <a style="left:357px">SERVICES OFFERED</a>
    <a style="left:437px">TASK FORCE &amp; CONSULTING</a>
    <a style="left:550px">TESTIMONIALS</a>
    <a style="left:617px">BLOG</a>
    <a style="left:652px">CONTACT ME</a>
    <svg style="position:absolute;left:713px;top:1px" width="7" height="7" viewBox="0 0 7 7"><circle cx="3" cy="3" r="2.2" stroke="#333" fill="none"/><path d="M4.6 4.6L6.6 6.6" stroke="#333"/></svg>
  </nav>
</header>

<section class="abs hero" role="img" aria-label="Concert crowd under bright orange stage lights"></section>
<div class="abs frame-outer"></div>
<div class="abs frame-inner"></div>
<h1 class="abs hero-title">Get your Event planned<br>with experts.</h1>
<div class="abs person" role="img" aria-label="Portrait of the event planner in a black blazer"></div>
<div class="abs btn">READ MORE</div>
<div class="abs arrow" style="left:8px"><svg width="6" height="8" viewBox="0 0 6 8"><path d="M5 0L1 4l4 4" stroke="#fff" fill="none"/></svg></div>
<div class="abs arrow" style="left:763px"><svg width="6" height="8" viewBox="0 0 6 8"><path d="M1 0l4 4-4 4" stroke="#fff" fill="none"/></svg></div>

<div class="abs feature" style="left:74px">
  <div class="icon"><svg width="14" height="14" viewBox="0 0 14 14"><path d="M1 6h3v7H1zM4 6l3-5c1 0 2 1 1.5 2.5L8 5h4c1 0 1.5 1 1 2l-1.5 5c-.3.7-.8 1-1.5 1H4" stroke="#333" fill="none"/></svg></div>
  <h3>CORPORATE EVENTS</h3>
  <p>Sed justo eros, cursus nec ultrice, trisque eget nisi. Fusce congue vestibulum lacin. at, placerat at leo. Donec sodales or.</p>
</div>
<div class="abs feature" style="left:241px">
  <div class="icon"><svg width="14" height="12" viewBox="0 0 14 12"><rect x="2.5" y="1" width="9" height="7" stroke="#333" fill="none"/><path d="M0 10h14" stroke="#333" stroke-width="1.5"/></svg></div>
  <h3>FAMILY EVENTS</h3>
  <p>Sed justo eros, cursus nec ultrice, trisque eget nisi. Fusce congue vestibulum lacin. at, placerat at leo. Donec sodales or.</p>
</div>
<div class="abs feature" style="left:408px">
  <div class="icon"><svg width="14" height="14" viewBox="0 0 14 14"><path d="M2 12l8-8" stroke="#333" stroke-width="2"/><path d="M11 1v3M9.5 2.5h3M12 6l1 1" stroke="#333"/></svg></div>
  <h3>SAVE YOUR TIME</h3>
  <p>Sed justo eros, cursus nec ultrice, trisque eget nisi. Fusce congue vestibulum lacin. at, placerat at leo. Donec sodales or.</p>
</div>
<div class="abs feature" style="left:574px">
  <div class="icon"><svg width="16" height="14" viewBox="0 0 16 14"><circle cx="6" cy="8" r="3.5" stroke="#333" stroke-width="2" stroke-dasharray="2 1.2" fill="none"/><circle cx="12" cy="4" r="2" stroke="#333" stroke-width="1.5" fill="none"/><circle cx="12.5" cy="11" r="1.5" stroke="#333" fill="none"/></svg></div>
  <h3>LOT OF EVENT DESIGNS</h3>
  <p>Sed justo eros, cursus nec ultrice, trisque eget nisi. Fusce congue vestibulum lacin. at, placerat at leo. Donec sodales or.</p>
</div>

<div class="abs rule"></div>
<h2 class="abs section-title" style="left:0;top:683px">THERE’S MORE TO A CORPORATE EVENT THAN THE WORDS YOU SAY.</h2>
<p class="abs section-text" style="top:709px">We know how to create an impression, underscore a message, and drive home a clear point using sound, video, lighting, and staging in powerful ways. Ways that take the ordinary and crank it<br>up to extraordinary so it looks and sounds incredible!</p>
<div class="abs boardroom" role="img" aria-label="Boardroom table with glasses, notepads and black leather chairs"></div>

<section class="abs showcase"></section>
<h2 class="abs section-title" style="left:0;top:1038px">OUR RECENT EVENTS SHOWCASE</h2>
<p class="abs section-text" style="top:1063px">Check out some of the latest events organized by Harlow.</p>
<div class="abs thumb" style="left:84px;background:linear-gradient(#4d5a3c,#8a7a5a 70%,#6a4a2a)" role="img" aria-label="Hiker walking on a wooden boardwalk in a forest"></div>
<div class="abs thumb" style="left:246px;background:linear-gradient(#111 0 8%,#e8e8e8 8%,#f0c0a8 80%,#e06040)" role="img" aria-label="Video still of red paint splash"><div class="play"><svg width="10" height="10" viewBox="0 0 10 10"><path d="M2 1l7 4-7 4z" fill="#fff"/></svg></div></div>
<div class="abs thumb" style="left:408px;background:linear-gradient(#4d5a3c,#8a7a5a 70%,#6a4a2a)" role="img" aria-label="Hiker walking on a wooden boardwalk in a forest"></div>
<div class="abs thumb" style="left:570px;background:linear-gradient(#111 0 8%,#2a6ec8 8%,#6aa8e8)" role="img" aria-label="Video still of a skier jumping against blue sky"><div class="play"><svg width="10" height="10" viewBox="0 0 10 10"><path d="M2 1l7 4-7 4z" fill="#fff"/></svg></div></div>
</body>
</html>
```